business card for Your Loan Scout

Please create a business card for my new business. I have attached another business card i have used previously and I like its layout and the hologram style backing with the logo. Replace the information with my new business information. On the information side of the card under the logo please place the TLCA acredited member logo I have uploaded along with 'Credit Rep Number 381749'.
next to my name in smaller text and not bold write 'JP'. and my title change from director to Broker/Director
Industry/Entity Type
Mortgage Brokerage
Contact Information for Business Card
As already on the uploaded card and in project description
Colors
Designer to choose colors to be used in the design.
Look and feel
Each slider illustrates characteristics of the customer's brand and the style your logo design should communicate.

```html
<!DOCTYPE html>
<html lang="en">
<head>
<meta charset="utf-8">
<title>Your Loan Scout – Business Card</title>
<link href="https://fonts.googleapis.com/css2?family=Cinzel:wght@600&family=Roboto:wght@300;400;700&display=swap" rel="stylesheet">
<style>
  :root {
    --backdrop: #1b2129;
    --card-black: #000000;
    --card-white: #ffffff;
    --brand-blue: #1b79c9;
    --brand-grey: #8a96a3;
    --ink: #1d1f22;
    --ink-soft: #8c8f93;
    --contact-ink: #1b2a4a;
    --badge-navy: #2a3a8c;
  }
  * { margin: 0; padding: 0; box-sizing: border-box; }
  html, body { width: 1200px; height: 1200px; overflow: hidden; }
  body { background: var(--backdrop); position: relative; font-family: "Roboto", sans-serif; }

  .card { position: absolute; left: 180px; width: 840px; overflow: hidden; }
  .card-front { top: 60px; height: 511px; background: var(--card-black); }
  .card-back { top: 644px; height: 504px; background: var(--card-white); }

  .notch { position: absolute; top: 134px; width: 46px; height: 251px; background: var(--card-white); }
  .notch-left { left: 0; border-radius: 0 40px 40px 0; }
  .notch-right { right: 0; border-radius: 40px 0 0 40px; }

  .brand { position: absolute; display: flex; flex-direction: column; align-items: center; }
  .brand-mark { background: var(--brand-blue); }
  .brand-name { font-family: "Cinzel", serif; font-weight: 600; color: var(--brand-blue); white-space: nowrap; line-height: 1; }

  .card-front .brand { left: 0; right: 0; top: 140px; }
  .card-front .brand-mark { width: 116px; height: 116px; margin-bottom: 40px; }
  .card-front .brand-name { font-size: 40px; }

  .back-panel { position: absolute; left: 0; top: 0; width: 336px; height: 100%; background: var(--card-black); }
  .back-panel .brand { left: 0; right: 0; top: 150px; }
  .back-panel .brand-mark { width: 84px; height: 84px; margin-bottom: 34px; }
  .back-panel .brand-name { font-size: 23px; }
  .partner-badge { position: absolute; left: 130px; top: 322px; width: 76px; height: 42px; border-radius: 6px; background: var(--badge-navy); }
  .credit-rep { position: absolute; left: 0; right: 0; top: 376px; text-align: center; font-size: 13px; font-weight: 400; color: var(--brand-grey); letter-spacing: 0.5px; }

  .person { position: absolute; left: 368px; top: 110px; width: 440px; text-align: center; }
  .person-name { font-size: 46px; font-weight: 700; color: var(--ink); letter-spacing: -1.5px; white-space: nowrap; line-height: 1.1; }
  .person-name .post-nominal { font-weight: 300; }
  .person-title { font-size: 27px; font-weight: 300; color: var(--ink-soft); margin-top: 2px; }

  .contacts { position: absolute; left: 318px; top: 274px; list-style: none; }
  .contact { display: flex; align-items: center; height: 38px; margin-bottom: 23px; }
  .contact-icon { width: 38px; height: 38px; border-radius: 50%; background: var(--brand-blue); display: flex; align-items: center; justify-content: center; margin-right: 24px; flex: none; }
  .contact-text { font-size: 25px; color: var(--contact-ink); letter-spacing: 0.5px; }
</style>
</head>
<body>
  <section class="card card-front">
    <div class="notch notch-left"></div>
    <div class="notch notch-right"></div>
    <div class="brand">
      <div class="brand-mark"></div>
      <div class="brand-name">Your Loan Scout</div>
    </div>
  </section>

  <section class="card card-back">
    <div class="back-panel">
      <div class="brand">
        <div class="brand-mark"></div>
        <div class="brand-name">Your Loan Scout</div>
      </div>
      <div class="partner-badge" role="img" aria-label="Accredited member badge"></div>
      <div class="credit-rep">Credit Rep Number 381749</div>
    </div>

    <div class="person">
      <div class="person-name">DANIEL HARTLEY <span class="post-nominal">JP</span></div>
      <div class="person-title">Broker/Director</div>
    </div>

    <ul class="contacts">
      <li class="contact">
        <span class="contact-icon">
          <svg width="20" height="20" viewBox="0 0 24 24" fill="#fff"><path d="M6.6 10.8a15.1 15.1 0 0 0 6.6 6.6l2.2-2.2c.3-.3.7-.4 1-.2 1.1.4 2.3.6 3.6.6.6 0 1 .4 1 1V20c0 .6-.4 1-1 1A17 17 0 0 1 3 4c0-.6.4-1 1-1h3.5c.6 0 1 .4 1 1 0 1.3.2 2.5.6 3.6.1.3 0 .7-.2 1z"/></svg>
        </span>
        <span class="contact-text">0400 555 218</span>
      </li>
      <li class="contact">
        <span class="contact-icon">
          <svg width="20" height="16" viewBox="0 0 24 18" fill="none" stroke="#fff" stroke-width="2"><rect x="1" y="1" width="22" height="16" rx="1" fill="#fff"/><path d="M1 1l11 9 11-9" stroke="#1b79c9"/></svg>
        </span>
        <span class="contact-text">dan@hartleyloans.com.au</span>
      </li>
      <li class="contact">
        <span class="contact-icon">
          <svg width="22" height="22" viewBox="0 0 24 24" fill="none" stroke="#fff" stroke-width="1.6"><circle cx="12" cy="12" r="10"/><ellipse cx="12" cy="12" rx="4.5" ry="10"/><path d="M2 12h20M4 6.5h16M4 17.5h16"/></svg>
        </span>
        <span class="contact-text">hartleyloans.com.au</span>
      </li>
    </ul>
  </section>
</body>
</html>
```